Construction Website Design for Wordpress

Update:
I like this theme as a starting point. It seems like a very good start. Fonts, colors, motion, etc. https://consultancy.qrvistaweb.com/
***************************************************************************************

I want a new website design that can be implemented in wordpress. Here is my existing site: www.halvornquantax.com
Attached is a document with the copy, requirements, sample images, etc. Let me know what questions you have.

Here is a sample of the info, but review the attached document for everything:

Website layout:
Title Bar
• Home
• Expertise
• Takeoffs
• Divisions Serviced (redesign from orig page: (http://www.halvornquantax.com/scope-list/)
• Member Login
Requirements
• Home page has a slider with 3 dimmed commercial construction images and copy overlay
• Request for Proposal Form should be over the slider and the same look and location on every page.
• “Request For Proposal” – No Obligation
o Company Name
o Contact Name
o Contact Phone
o Contact Email
• Use the copy below for the pages
• Split the Client Testimonials among the pages

Target Market(s)

B2B - Construction Companies

Industry/Entity Type

Construction

Number of Pages Required

4 page

Font styles to use
Serif

Colors
0255a3
3276b5
85abd2
d0dfed

Requirements
Must have
• Construction images in slider
• Request for proposal form
• testimonials

```html
<!DOCTYPE html>
<html lang="en">
<head>
<meta charset="utf-8">
<title>Halvorn Quantax — Construction Takeoff Experts</title>
<link href="https://fonts.googleapis.com/css2?family=Montserrat:wght@400;500;600;700&family=Ubuntu:ital,wght@0,400;0,500;1,400&display=swap" rel="stylesheet">
<style>
:root{
  --navy:#0a3c74;
  --navy-deep:#083466;
  --accent:#3a9ad9;
  --ink:#1d1d1d;
  --body:#4a4a4a;
  --field:#ececec;
  --band:#f0f1f0;
  --white:#ffffff;
}
*{margin:0;padding:0;box-sizing:border-box}
html,body{width:1200px;height:2273px;overflow:hidden}
body{position:relative;background:var(--white);font-family:"Ubuntu",sans-serif;color:var(--body)}
.abs{position:absolute}

/* header */
.site-header{left:0;top:0;width:1200px;height:88px;background:var(--white)}
.brand{left:86px;top:24px;display:flex;align-items:center;gap:10px}
.brand-mark{width:14px;height:14px;border:2px solid var(--accent);border-radius:50%}
.brand-name{font-family:"Montserrat",sans-serif;font-weight:600;font-size:25px;color:var(--navy);letter-spacing:.5px;text-transform:uppercase}
.main-nav{left:568px;top:33px;display:flex;gap:26px;font-family:"Montserrat",sans-serif;font-size:13px;color:var(--ink);font-weight:500}
.login-btn{left:962px;top:22px;width:153px;height:41px;border-radius:21px;background:var(--navy);color:var(--white);font-family:"Montserrat",sans-serif;font-size:14px;display:flex;align-items:center;justify-content:center}

/* hero */
.hero{left:0;top:88px;width:1200px;height:450px;background:linear-gradient(115deg,#d8dde3 0%,#eef0f2 40%,#c9ced4 75%,#e4e6e8 100%)}
.hero-caption{left:0;top:376px;width:502px;height:162px;background:var(--navy)}
.hero-caption h2{position:absolute;left:38px;top:20px;font-family:"Montserrat",sans-serif;font-weight:700;font-size:29px;color:var(--white);letter-spacing:.5px}
.hero-caption .rule{position:absolute;left:0;top:62px;width:240px;height:2px;background:var(--accent)}
.hero-caption p{position:absolute;left:38px;top:74px;width:430px;font-size:19px;line-height:30px;color:var(--white)}
.dots{left:569px;top:505px;display:flex;gap:10px}
.dots span{width:14px;height:14px;border-radius:50%;border:2px solid var(--white)}
.dots span.on{background:var(--navy);border-color:var(--navy)}

.rfp{left:723px;top:145px;width:353px;height:337px;background:var(--white);box-shadow:0 2px 10px rgba(0,0,0,.12)}
.rfp h3{position:absolute;left:0;top:30px;width:100%;text-align:center;font-family:"Ubuntu",sans-serif;font-weight:500;font-size:23px;color:var(--ink);letter-spacing:.3px}
.rfp .field{position:absolute;left:36px;width:282px;height:37px;background:var(--field);font-size:11px;color:#777;display:flex;align-items:center;justify-content:center}
.rfp .send{position:absolute;left:36px;top:263px;width:282px;height:37px;background:var(--navy);color:var(--white);font-size:15px;font-weight:500;display:flex;align-items:center;justify-content:center}

/* about */
.about-title{left:85px;top:642px;font-family:"Montserrat",sans-serif;font-weight:500;font-size:35px;color:var(--ink)}
.about-rule{left:0;top:692px;width:376px;height:1px;background:#bdbdbd}
.about-copy{left:86px;top:723px;width:484px;font-size:13.8px;line-height:25.5px;color:var(--body)}
.about-copy p{margin-bottom:26px}
.about-copy h4{font-family:"Montserrat",sans-serif;font-weight:600;font-size:15px;color:var(--navy);text-decoration:underline;margin:-6px 0 4px -2px}
.about-copy p.tight{margin-bottom:22px}
.about-photo{left:589px;top:652px;width:526px;height:584px;background:linear-gradient(150deg,#7d8fa6 0%,#aebccb 35%,#dfe3e8 60%,#9aa7b4 100%)}

/* testimonials */
.testimonials{left:0;top:1348px;width:1200px;height:649px;background:var(--band)}
.testimonials h2{position:absolute;left:0;top:104px;width:100%;text-align:center;font-family:"Montserrat",sans-serif;font-weight:500;font-size:35px;color:var(--ink)}
.quote-card{top:241px;width:391px;height:297px;background:var(--white);border-radius:3px}
.avatar{position:absolute;left:139px;top:-51px;width:113px;height:113px;border-radius:50%;border:5px solid var(--white);background:linear-gradient(160deg,#c9ccd0,#8c9096)}
.quote-card blockquote{position:absolute;left:26px;top:77px;width:339px;text-align:center;font-style:italic;font-size:14px;line-height:23px;color:#555}
.quote-card blockquote.narrow{left:48px;width:295px}
.quote-card .who{position:absolute;left:0;width:100%;text-align:center;font-family:"Montserrat",sans-serif;color:var(--ink)}
.who .name{font-size:15px;font-weight:500}
.who .role{font-size:11.5px;margin:4px 0}
.who .org{font-size:15px;font-weight:500}

/* footer */
.site-footer{left:0;top:1997px;width:1200px;height:276px;background:var(--navy-deep);color:var(--white)}
.social{position:absolute;left:500px;top:90px;display:flex;gap:9px}
.social span{width:43px;height:43px;border-radius:50%;border:2px solid var(--white)}
.contact{position:absolute;left:0;top:162px;width:100%;display:flex;justify-content:center;align-items:center;gap:10px;font-size:13px}
.contact svg{fill:var(--white);vertical-align:-2px;margin-right:5px}
.footer-nav{position:absolute;left:0;top:192px;width:100%;text-align:center;font-size:14.5px;color:#dfe6ef;word-spacing:2px}
.footer-nav span{margin:0 12px}
.copyright{position:absolute;left:0;top:225px;width:100%;text-align:center;font-size:13px}
</style>
</head>
<body>

<header class="site-header abs">
  <div class="brand abs"><span class="brand-mark"></span><span class="brand-name">Halvorn Quantax</span></div>
  <nav class="main-nav abs"><span>Home</span><span>Expertise</span><span>Takeoffs</span><span>Divisions Serviced</span></nav>
  <div class="login-btn abs">Member Login</div>
</header>

<section class="hero abs" role="img" aria-label="Dimmed photo of hands reviewing construction blueprints on a desk"></section>

<div class="hero-caption abs">
  <h2>CONFIDENCE</h2>
  <div class="rule"></div>
  <p>– Accurate and reliable, we help you propose on more work without risk.</p>
</div>
<div class="dots abs"><span class="on"></span><span></span><span></span></div>

<form class="rfp abs">
  <h3>REQUEST FOR PROPOSAL</h3>
  <div class="field" style="top:78px">Company Name</div>
  <div class="field" style="top:125px">Contact Name</div>
  <div class="field" style="top:170px">Contact Phone</div>
  <div class="field" style="top:217px">Contact Email</div>
  <div class="send">Send A Request</div>
</form>

<h1 class="about-title abs">Halvorn Quantax</h1>
<div class="about-rule abs"></div>
<div class="about-copy abs">
  <p>Dedicated to saving our clients time and money by specializing in accurate, reliable materials quantity calculations, Halvorn Quantax allows general contractors to confidently propose on more work with less stress.</p>
  <p class="tight">To receive a no-obligation answer to your takeoff needs complete the Request for Proposal form. Halvorn Quantax will provide a comprehensive proposal detailing the hours required and payment options that are easily refined to both near- and long-term needs.</p>
  <h4>PROCESS:</h4>
  <p class="tight">Once the proposal is approved, clients fund their account and allocate their hours as desired - project-by-project, monthly, as-needed, or otherwise. Our service and products are completely tailored to each client based on the fundamental factors that make your business distinct from all others.</p>
  <h4>BENEFITS:</h4>
  <p>Accurate, reliable quantities delivered as-scheduled and expected allow your key staff to invest their time in quality, safety, profit, and client relationships. An extra set of hands in your bid room helps you put out more proposals and takes a tedious task off your to-do list whenever you need it without the obligation of a full-time salary.</p>
</div>
<div class="about-photo abs" role="img" aria-label="Photo of an estimator working on a laptop beside rolled construction plans"></div>

<section class="testimonials abs">
  <h2>What Clients Say</h2>
  <article class="quote-card abs" style="left:185px">
    <div class="avatar" role="img" aria-label="Portrait photo of the client"></div>
    <blockquote>“Halvorn Quantax does outstanding work, accurate, detailed, and reliable. The consultant on my account knows what I want in the breakdown and produces the information exactly as I need it. Time, money and confidence, Halvorn Quantax hits the mark every time.”</blockquote>
    <div class="who" style="top:216px"><div class="name">Dana Whitfield,</div><div class="role">President</div><div class="org">Crestline Roofing</div></div>
  </article>
  <article class="quote-card abs" style="left:624px">
    <div class="avatar" role="img" aria-label="Portrait photo of the client"></div>
    <blockquote class="narrow">“We get an influx of great opportunities and sometimes it’s more than we can handle. Halvorn Quantax fills the gap and helped us to grow our business. It’s really excellent to have a genuine, always-ready ally in our estimating efforts.”</blockquote>
    <div class="who" style="top:216px"><div class="name">Marco Velden</div><div class="org" style="margin-top:2px">Northgate Builders, LLC.</div></div>
  </article>
</section>

<footer class="site-footer abs">
  <div class="social" aria-label="Social links"><span></span><span></span><span></span><span></span></div>
  <div class="contact">
    <span><svg width="10" height="13" viewBox="0 0 10 13"><path d="M5 0a5 5 0 0 0-5 5c0 3.5 5 8 5 8s5-4.5 5-8a5 5 0 0 0-5-5zm0 7a2 2 0 1 1 0-4 2 2 0 0 1 0 4z"/></svg>Halvorn Quantax, Construction, KT4 7PL</span><span>|</span>
    <span><svg width="12" height="12" viewBox="0 0 12 12"><path d="M2.4 0.5 4.3 2.6 3.3 4.2c.8 1.8 2.3 3.3 4.5 4.5l1.6-1 2.1 1.9-1.3 2C5 11.6.3 6.8 0.4 1.7z"/></svg>0800 555 0142</span><span>|</span>
    <span><svg width="14" height="11" viewBox="0 0 14 11"><path d="M0 0h14v1.5L7 6 0 1.5zM0 3.2 7 7.7l7-4.5V11H0z"/></svg>info@halvornquantax.com</span>
  </div>
  <nav class="footer-nav"><span>Home</span>|<span>Expertise</span>|<span>Takeoffs</span>|<span>Divisions Serviced</span></nav>
  <p class="copyright">Copyrights © 2019, Halvorn Quantax. All rights reserved.</p>
</footer>

</body>
</html>
```